Project Title:
Dental Implant Overdenture Flyer (Retirement Village Target)
Objective:
Create a clean, trustworthy, and reassuring flyer aimed at older adults (60–85 years old) who struggle with loose dentures. The goal is to educate them about implant-retained “clip-on” dentures and encourage them to book a consultation.
Tone & Feel:
Warm, caring, non-intimidating
Premium but not “salesy”
Medical but easy to understand
Focus on improving quality of life (confidence, eating, comfort)
Target Audience:
Retirees / pensioners
Existing denture wearers
People frustrated with loose or uncomfortable dentures
Key Message:
“You don’t have to live with loose dentures anymore.”
Design Style:
Clean, minimal, modern
Soft colours (blues, greens, warm neutrals)
Easy-to-read large font
High contrast for older eyes
Avoid clutter
Imagery Suggestions:
Smiling older adults (natural, not stocky/overly staged)
Before/after lifestyle (eating, laughing, socialising)
Simple diagram showing denture clipping onto implants
Avoid graphic surgical images
Layout Suggestions:
A5 or DL flyer
Clear sections with headings
Icons for benefits
Strong call-to-action at bottom
HEADLINE (big and bold)
Tired of Loose Dentures?
Discover Secure “Clip-On” Teeth
🔹 PROBLEM SECTION
Do your dentures:
Slip or move when eating?
Make it hard to chew certain foods?
Feel uncomfortable or loose?
Affect your confidence when speaking or smiling?
You’re not alone — and there is a better solution.
🔹 SOLUTION SECTION
Implant-Retained “Clip-On” Dentures
We can secure your denture using just 2 dental implants, allowing your teeth to:
✔ Stay firmly in place
✔ Improve your ability to eat
✔ Feel more comfortable
✔ Boost your confidence
🔹 SIMPLE EXPLANATION (very important)
Small titanium implants are gently placed in the jaw.
Your denture then clips securely onto them, stopping movement.
🔹 PRICE SECTION (highlight this clearly)
$12,000
Includes:
2 dental implants
A brand new custom overdenture
Does not include sedation or extractions (if needed)
🔹 SEDATION
Sedation is available for comfort.
If you hold a pensioner card, you may receive a significant Vantacor rebate, often resulting in minimal out-of-pocket costs for sedation.
🔹 TRUST / REASSURANCE
Experienced implant clinician
Gentle, patient-focused care
Modern technology and techniques
🔹 CALL TO ACTION (VERY IMPORTANT)
Book a Free Consultation
📞 Call: 08 9351 4276
🌐 Visit: www.bravonclinic.com.au
📍 Located near Tallowmere shopping centre
🔹 OPTIONAL TAGLINE
Eat Better. Feel Better. Smile with Confidence Again.
Please include some photos to illustrate what a clip on denture looks like with two implants.

```html
<!DOCTYPE html>
<html lang="en">
<head>
<meta charset="utf-8">
<title>Bravon Clinic – Clip-On Dentures Flyer</title>
<link href="https://fonts.googleapis.com/css2?family=Montserrat:wght@500;600;700;800&family=Open+Sans:wght@400;600;700&display=swap" rel="stylesheet">
<style>
  :root {
    --navy: #1d3557;
    --teal: #2596b0;
    --teal-dark: #17748a;
    --band: #1c7c93;
    --panel: #e5f2f6;
    --text: #2d3a45;
    --white: #ffffff;
    --photo-a: #b9a48f;
    --photo-b: #6f8796;
  }
  * { box-sizing: border-box; margin: 0; padding: 0; }
  html, body { width: 896px; height: 1200px; overflow: hidden; background: var(--white); }
  body { font-family: "Open Sans", Arial, sans-serif; color: var(--text); }
  .flyer { position: relative; width: 896px; height: 1200px; overflow: hidden; background: var(--white); }

  .brand { position: absolute; left: 40px; top: 36px; display: flex; align-items: center; gap: 12px; }
  .brand-mark { width: 34px; height: 34px; border-radius: 50%; background: var(--teal); }
  .brand-name { font-family: "Montserrat", Arial, sans-serif; font-weight: 700; font-size: 22px; color: var(--navy); line-height: 1.05; letter-spacing: .5px; }

  .headline { position: absolute; left: 420px; top: 34px; width: 450px; font-family: "Montserrat", Arial, sans-serif; }
  .headline .kicker { font-size: 29px; font-weight: 700; color: var(--teal); line-height: 1.2; }
  .headline .main { font-size: 29px; font-weight: 800; color: var(--navy); line-height: 1.2; }

  .left-col { position: absolute; left: 40px; top: 180px; width: 330px; font-size: 17px; line-height: 1.45; }
  .left-col h2 { font-family: "Montserrat", Arial, sans-serif; font-size: 27px; font-weight: 700; color: var(--teal); margin-bottom: 16px; }
  .problem-list { list-style: none; }
  .problem-list li { margin-bottom: 14px; }
  .not-alone { color: var(--teal); font-weight: 700; margin: 6px 0 26px; }
  .explain { margin-bottom: 34px; }
  .price { font-family: "Montserrat", Arial, sans-serif; font-size: 36px; font-weight: 700; color: var(--teal); line-height: 1; margin-bottom: 12px; }
  .includes { margin-bottom: 16px; }
  .excludes { margin-bottom: 18px; }
  .sedation-title { font-weight: 700; margin-bottom: 14px; }
  .sedation-text { font-size: 16px; }

  .cta { position: absolute; left: 40px; top: 982px; font-family: "Montserrat", Arial, sans-serif; font-size: 28px; font-weight: 700; color: var(--teal); }

  .solution-panel { position: absolute; left: 410px; top: 180px; width: 456px; height: 350px; background: var(--panel); border-radius: 6px; padding: 26px 28px; }
  .solution-panel h3 { font-family: "Montserrat", Arial, sans-serif; font-size: 18px; font-weight: 700; color: var(--teal-dark); margin-bottom: 26px; }
  .solution-panel p { font-size: 17px; line-height: 1.45; margin-bottom: 18px; }
  .benefits { list-style: none; }
  .benefits li { display: flex; align-items: center; gap: 14px; font-weight: 700; font-size: 17px; color: var(--navy); margin-bottom: 12px; }
  .benefits svg { flex: none; }

  .photo { position: absolute; }
  .photo-patients { left: 410px; top: 530px; width: 486px; height: 230px; background: linear-gradient(90deg, var(--photo-a) 0%, #d7c8b6 50%, var(--photo-b) 100%); }
  .photo-clinician { left: 610px; top: 760px; width: 270px; height: 350px; background: linear-gradient(180deg, #c9d6dd 0%, #8da3b1 60%, #3f5666 100%); z-index: 2; }

  .trust { position: absolute; left: 410px; top: 790px; width: 220px; list-style: none; font-size: 16px; line-height: 1.35; }
  .trust li { display: flex; gap: 10px; margin-bottom: 18px; }
  .trust .dot { flex: none; width: 10px; height: 10px; margin-top: 6px; border-radius: 50%; background: var(--teal); }

  .contact-band { position: absolute; left: 0; top: 1030px; width: 896px; height: 170px; }
  .contact-band svg.band-shape { position: absolute; inset: 0; }
  .contact-list { position: absolute; left: 110px; top: 66px; list-style: none; color: var(--white); font-size: 18px; font-weight: 600; z-index: 1; }
  .contact-list li { display: flex; align-items: center; gap: 14px; margin-bottom: 10px; }
</style>
</head>
<body>
<div class="flyer">

  <div class="brand">
    <span class="brand-mark"></span>
    <span class="brand-name">BRAVON CLINIC<br>DENTAL SURGERY</span>
  </div>

  <header class="headline">
    <div class="kicker">Tired of Loose Dentures?</div>
    <div class="main">Discover Secure “Clip-On” Teeth</div>
  </header>

  <section class="left-col">
    <h2>Do your dentures:</h2>
    <ul class="problem-list">
      <li>Slip or move when eating?<br>Make it hard to chew certain foods?</li>
      <li>Feel uncomfortable or loose?<br>Affect your confidence when speaking or smiling?</li>
    </ul>
    <p class="not-alone">You’re not alone — and there is a better solution.</p>
    <p class="explain">Small titanium implants are gently placed in the jaw. Your denture then clips securely onto them, stopping movement.</p>
    <div class="price">$12,000</div>
    <p class="includes">Includes:<br>2 dental implants<br>A brand new custom overdenture</p>
    <p class="excludes">Does not include sedation or extractions (if needed)</p>
    <p class="sedation-title">Sedation is available for comfort.</p>
    <p class="sedation-text">If you hold a pensioner card, you may receive a significant Vantacor rebate, often resulting in minimal out-of-pocket costs for sedation.</p>
  </section>

  <div class="cta">Book a Free Consultation</div>

  <section class="solution-panel">
    <h3>Implant-Retained “Clip-On” Dentures</h3>
    <p>We can secure your denture using just 2 dental implants, allowing your teeth to:</p>
    <ul class="benefits">
      <li><svg width="12" height="14" viewBox="0 0 12 14"><path d="M0 0 L12 7 L0 14 Z" fill="#2596b0"/></svg>Stay firmly in place</li>
      <li><svg width="12" height="14" viewBox="0 0 12 14"><path d="M0 0 L12 7 L0 14 Z" fill="#2596b0"/></svg>Improve your ability to eat</li>
      <li><svg width="12" height="14" viewBox="0 0 12 14"><path d="M0 0 L12 7 L0 14 Z" fill="#2596b0"/></svg>Feel more comfortable</li>
      <li><svg width="12" height="14" viewBox="0 0 12 14"><path d="M0 0 L12 7 L0 14 Z" fill="#2596b0"/></svg>Boost your confidence</li>
    </ul>
  </section>

  <div class="photo photo-patients" role="img" aria-label="Two smiling older men, side by side, showing confident natural smiles"></div>

  <ul class="trust">
    <li><span class="dot"></span>Experienced implant clinician</li>
    <li><span class="dot"></span>Gentle, patient-focused care</li>
    <li><span class="dot"></span>Modern technology and techniques</li>
  </ul>

  <div class="photo photo-clinician" role="img" aria-label="Smiling implant clinician in a dark shirt with arms folded"></div>

  <footer class="contact-band">
    <svg class="band-shape" width="896" height="170" viewBox="0 0 896 170" aria-hidden="true">
      <path d="M0 30 Q448 -10 896 40 L896 170 L0 170 Z" fill="#1c7c93"/>
      <path d="M0 30 Q448 -10 896 40" fill="none" stroke="#2596b0" stroke-width="6"/>
    </svg>
    <ul class="contact-list">
      <li>
        <svg width="20" height="20" viewBox="0 0 24 24"><path d="M6.6 10.8a15 15 0 0 0 6.6 6.6l2.2-2.2a1 1 0 0 1 1-.25 11.4 11.4 0 0 0 3.6.6 1 1 0 0 1 1 1V20a1 1 0 0 1-1 1A17 17 0 0 1 3 4a1 1 0 0 1 1-1h3.5a1 1 0 0 1 1 1c0 1.25.2 2.45.6 3.6a1 1 0 0 1-.25 1z" fill="#fff"/></svg>
        08 9351 4276
      </li>
      <li>
        <svg width="20" height="20" viewBox="0 0 24 24"><circle cx="12" cy="12" r="9" fill="none" stroke="#fff" stroke-width="2"/><path d="M3 12h18M12 3c3 3 3 15 0 18M12 3c-3 3-3 15 0 18" fill="none" stroke="#fff" stroke-width="1.6"/></svg>
        www.bravonclinic.com.au
      </li>
      <li>
        <svg width="20" height="20" viewBox="0 0 24 24"><path d="M12 2a7 7 0 0 0-7 7c0 5 7 13 7 13s7-8 7-13a7 7 0 0 0-7-7zm0 9.5A2.5 2.5 0 1 1 12 6.5a2.5 2.5 0 0 1 0 5z" fill="#fff"/></svg>
        Located near Tallowmere shopping centre
      </li>
    </ul>
  </footer>

</div>
</body>
</html>
```